出産内祝いのはがきの作成をお願いします。通信欄(片面です。)、良いものであれば、複数採用いたします。何か質問があればご連絡ください。用紙は縦向きです
子供の名前と、体重、誕生日。メッセージ。
写真を入れる場合と入れない場合をお願いします。
はがきサイズ タテ

お世話になります。

スタッフの意見により決定いたしました。

素晴らしいご提案ありがとうございます。

今後ともよろしくお願いいたします。

```html
<!DOCTYPE html>
<html lang="ja">
<head>
<meta charset="UTF-8">
<title>出産内祝い はがき</title>
<link href="https://fonts.googleapis.com/css2?family=Pacifico&family=Kosugi+Maru&family=Klee+One:wght@600&display=swap" rel="stylesheet">
<style>
  :root {
    --frame-blue: #6fc6d9;
    --script-blue: #62bccf;
    --ink: #5b4d46;
    --rule: #8a7d76;
    --paper: #ffffff;
    --photo-tone: #efe1d6;
    --photo-shade: #d9c3b2;
    --pink-tone: #f6cfcb;
    --pink-edge: #fbeeed;
    --purple-tone: #d3bde0;
    --purple-edge: #f3edf7;
    --blue-leaf-tone: #9cc9de;
    --blue-leaf-edge: #eef6fa;
  }
  * { margin: 0; padding: 0; box-sizing: border-box; }
  html, body { width: 810px; height: 1200px; overflow: hidden; background: var(--paper); }
  .card {
    position: relative;
    width: 810px;
    height: 1200px;
    background: var(--paper);
    border: 20px solid var(--frame-blue);
    font-family: "Kosugi Maru", sans-serif;
    color: var(--ink);
  }
  .card > * { position: absolute; }
  .baby-photo {
    left: 292px; top: 40px;
    width: 460px; height: 460px;
    border-radius: 50%;
    background: radial-gradient(circle at 50% 45%, var(--photo-tone) 0%, var(--photo-shade) 100%);
  }
  .greeting {
    font-family: "Pacifico", cursive;
    color: var(--script-blue);
    line-height: 1;
  }
  .greeting-hello { left: 48px; top: 118px; font-size: 92px; transform: rotate(-4deg); }
  .greeting-baby { left: 118px; top: 238px; font-size: 62px; transform: rotate(-3deg); }
  .illustration { border-radius: 24px; }
  .illustration-pink {
    left: 42px; top: 395px; width: 170px; height: 160px;
    background: radial-gradient(ellipse at 60% 45%, var(--pink-tone) 0%, var(--pink-edge) 75%, transparent 100%);
  }
  .illustration-purple {
    left: 545px; top: 580px; width: 200px; height: 160px;
    background: radial-gradient(ellipse at 45% 45%, var(--purple-tone) 0%, var(--purple-edge) 75%, transparent 100%);
  }
  .illustration-leaf {
    left: 600px; top: 40px; width: 130px; height: 100px;
    background: radial-gradient(ellipse at 50% 50%, var(--blue-leaf-tone) 0%, var(--blue-leaf-edge) 75%, transparent 100%);
  }
  .naming-label { left: 80px; top: 598px; font-size: 28px; letter-spacing: 2px; }
  .name-reading { top: 662px; font-size: 22px; letter-spacing: 4px; }
  .name-reading-family { left: 92px; }
  .name-reading-given { left: 300px; }
  .baby-name { left: 80px; top: 692px; font-family: "Klee One", serif; font-weight: 600; font-size: 64px; line-height: 76px; letter-spacing: 6px; }
  .baby-name .given { margin-left: 40px; }
  .rule { left: 80px; width: 650px; height: 2px; background: var(--rule); }
  .rule-name { top: 776px; }
  .rule-date { top: 846px; }
  .rule-stats { top: 922px; }
  .birth-date { left: 88px; top: 792px; font-size: 32px; line-height: 40px; letter-spacing: 10px; }
  .stats-divider { left: 405px; top: 852px; width: 2px; height: 66px; background: var(--rule); }
  .birth-weight { left: 88px; top: 864px; font-size: 32px; line-height: 40px; letter-spacing: 10px; }
  .birth-length { left: 455px; top: 864px; font-size: 32px; line-height: 40px; letter-spacing: 10px; }
  .thanks-message { left: 88px; top: 944px; font-size: 25px; line-height: 37px; letter-spacing: 3px; }
</style>
</head>
<body>
<main class="card">
  <div class="baby-photo" role="img" aria-label="赤ちゃんの写真"></div>
  <div class="illustration illustration-leaf" role="img" aria-label="青い葉のイラスト"></div>
  <div class="greeting greeting-hello">Hello</div>
  <div class="greeting greeting-baby">baby</div>
  <div class="illustration illustration-pink" role="img" aria-label="ピンクのダリアと葉のイラスト"></div>
  <div class="illustration illustration-purple" role="img" aria-label="紫のダリアと葉のイラスト"></div>

  <div class="naming-label">命名</div>
  <div class="name-reading name-reading-family">あおば</div>
  <div class="name-reading name-reading-given">ようた</div>
  <div class="baby-name"><span class="family">青葉</span><span class="given">陽太</span></div>
  <div class="rule rule-name"></div>

  <div class="birth-date">2011年8月31日生まれ</div>
  <div class="rule rule-date"></div>

  <div class="birth-weight">3200g</div>
  <div class="stats-divider"></div>
  <div class="birth-length">50.3 cm</div>
  <div class="rule rule-stats"></div>

  <p class="thanks-message">この度はお祝い頂き<br>誠にありがとうございます。<br>おかげ様をもちまして母子ともに元気に<br>過ごしています。また遊びに行きますので<br>今後ともよろしくお願いします。</p>
</main>
</body>
</html>
```